Business Card for premium dental clinic

We are a premium dental clinic based in Brasov, Romania with more than 15 year on the market, providing quality dental treatment made by a team of more specialized dentists, working with modern equipment as a solution to beautiful and healthy teeth.

Our current logo for the clinic use 2 square with colors black and gold - dr Merinca - studio, using family fonts Bodoni, Myriad Pro and Segoe Print.
Depending on the printing we used some gold CMYK background or gold foil picture background or a gold gradient.
We want a business card:
- eye catching business card
- distinguished business card
- premium design
- to keep the color scheme of black and gold
- to attract the customers to spent time reading the information
- modern concept

```html
<!DOCTYPE html>
<html lang="en">
<head>
<meta charset="UTF-8">
<title>Merinca Dental · Business Card</title>
<link rel="stylesheet" href="https://fonts.googleapis.com/css2?family=Fira+Sans+Condensed:wght@400&family=Montserrat:wght@500;600&display=swap">
<style>
  :root {
    --canvas: #e9e6e1;
    --card-black: #2b2b2d;
    --card-black-deep: #232325;
    --emboss: #1b1b1d;
    --gold-light: #f3c841;
    --gold-mid: #dca820;
    --gold-deep: #b7820c;
    --label-white: #ffffff;
    --ink: #1e1e1e;
    --text-light: #f2f2f2;
  }
  * { margin: 0; padding: 0; box-sizing: border-box; }
  html, body { width: 1200px; height: 800px; overflow: hidden; }
  body {
    background: var(--canvas);
    font-family: "Montserrat", Arial, sans-serif;
    position: relative;
  }
  .card {
    position: absolute;
    top: 257px;
    width: 500px;
    height: 286px;
    border-radius: 4px;
    overflow: hidden;
    box-shadow: 0 10px 24px rgba(0,0,0,0.18);
  }
  /* Back side */
  .card--back {
    left: 70px;
    background: var(--card-black);
  }
  .card--back .clinic-name {
    position: absolute;
    left: 0; right: 0;
    top: 110px;
    text-align: center;
    font-size: 48px;
    font-weight: 600;
    letter-spacing: 0.5px;
    color: var(--emboss);
  }
  /* Front side */
  .card--front {
    left: 630px;
    background: var(--card-black);
  }
  .gold-field {
    position: absolute;
    left: 0; top: 0;
    width: 292px; height: 100%;
    background:
      radial-gradient(ellipse at 30% 25%, var(--gold-light) 0%, transparent 55%),
      radial-gradient(ellipse at 75% 80%, var(--gold-light) 0%, transparent 50%),
      linear-gradient(135deg, var(--gold-mid) 0%, var(--gold-deep) 45%, var(--gold-mid) 70%, var(--gold-deep) 100%);
  }
  .name-label {
    position: absolute;
    left: 62px;
    top: 112px;
    width: 230px;
    height: 56px;
    background: var(--label-white);
    display: flex;
    align-items: center;
    padding-left: 18px;
    font-family: "Fira Sans Condensed", "Arial Narrow", sans-serif;
    color: var(--ink);
    font-size: 40px;
    line-height: 1;
  }
  .name-label .title { font-size: 26px; margin-right: 6px; align-self: flex-end; margin-bottom: 13px; }
  .info-panel {
    position: absolute;
    left: 292px; top: 0;
    width: 208px; height: 100%;
    background: var(--card-black-deep);
    padding: 90px 0 0 18px;
  }
  .info-panel .clinic-name {
    font-size: 21px;
    font-weight: 600;
    color: var(--gold-mid);
    margin: 0 0 24px 4px;
    white-space: nowrap;
  }
  .contacts { list-style: none; }
  .contacts li {
    display: flex;
    align-items: center;
    gap: 8px;
    color: var(--text-light);
    font-size: 12px;
    font-weight: 500;
    margin-bottom: 6px;
    white-space: nowrap;
  }
  .contacts svg { width: 12px; height: 12px; flex: none; fill: var(--text-light); }
</style>
</head>
<body>

  <section class="card card--back" aria-label="Card back">
    <div class="clinic-name">Merinca Dental</div>
  </section>

  <section class="card card--front" aria-label="Card front">
    <div class="gold-field" role="img" aria-label="Gold foil texture background"></div>
    <div class="name-label"><span class="title">dr.</span>Merinca</div>

    <div class="info-panel">
      <div class="clinic-name">Merinca Dental</div>
      <ul class="contacts">
        <li>
          <svg viewBox="0 0 24 24" aria-hidden="true"><path d="M6.6 10.8a15.1 15.1 0 0 0 6.6 6.6l2.2-2.2a1 1 0 0 1 1-.25 11.4 11.4 0 0 0 3.6.57 1 1 0 0 1 1 1V20a1 1 0 0 1-1 1A17 17 0 0 1 3 4a1 1 0 0 1 1-1h3.5a1 1 0 0 1 1 1c0 1.25.2 2.45.57 3.57a1 1 0 0 1-.25 1z"/></svg>
          0268-555-210
        </li>
        <li>
          <svg viewBox="0 0 24 24" aria-hidden="true"><path d="M2 5h20v14H2z M4 7v.5l8 5 8-5V7l-8 5z" fill-rule="evenodd"/></svg>
          hello@merincadental.ro
        </li>
        <li>
          <svg viewBox="0 0 24 24" aria-hidden="true"><circle cx="12" cy="12" r="9" fill="none" stroke="currentColor" stroke-width="2" style="stroke:var(--text-light)"/><path d="M3 12h18M12 3c3 3 3 15 0 18M12 3c-3 3-3 15 0 18" fill="none" style="stroke:var(--text-light)" stroke-width="1.6"/></svg>
          www.merincadental.ro
        </li>
      </ul>
    </div>
  </section>

</body>
</html>
```